Mobile Landing Page for giveaway Seedbombs done from a institution for handicaped people

We are a social institution that makes seedbombs that contain wildflowers for bees and other insects. During a sutanibel event, these bombs are given to an audience. On the packaging of the seedbombs, there is a QR code that leads to a landing page. We are producing a video showing how our handicapped clients made the seebombs. The Landigpage should look: sustanible, green, and sozial. On the page, there shoud be this Video, a manual how tho use the seedbombs. Something about our work whith the handicapt people a linkt to our Instagram amd a possibility to get involved whith us as well as a donation button. You can find more information about us on: www.talmatte-kollektiv.ch

Target Market(s)

People that are intressetet in envirement and social impakt

Industry/Entity Type

Social Impakt, Urban Gardening

Coding

Coded - Design and coding required

Number of Pages Required

1 page

Font styles to use
Other font styles liked:
• Joanna

Requirements
Must have
• Be optimised for smartphone
Nice to have
• like a floating page, witch leads you throug the different steps, mabey like a plant with ist growing. From the Bombs to the Plan. Or a little game ore something.

```html
<!DOCTYPE html>
<html lang="de">
<head>
<meta charset="utf-8">
<title>Talmatte – Seedbombs</title>
<link href="https://fonts.googleapis.com/css2?family=Gelasio:wght@400;600;700&family=Jost:wght@400;500;600&display=swap" rel="stylesheet">
<style>
:root{
  --forest:#22392c;
  --sage:#a9b89a;
  --blush:#f8e3da;
  --paper:#f2f0ea;
  --coral:#c9564a;
  --ink:#23352a;
  --photo-a:#7d9a5c;
  --photo-b:#c9d27a;
}
*{box-sizing:border-box;margin:0;padding:0}
html,body{width:1200px;height:3947px;overflow:hidden}
body{background:var(--paper);font-family:"Jost",sans-serif;color:var(--ink);position:relative}
.backdrop{position:absolute;left:0;top:0;width:1200px;height:497px;background:var(--sage)}
.title-mark{position:absolute;left:0;width:1200px;top:44px;text-align:center;font-family:"Gelasio",serif;font-size:52px;letter-spacing:3px;color:var(--forest);font-weight:600;padding-right:330px}
.serif{font-family:"Gelasio",serif}
.photo{background:linear-gradient(135deg,var(--photo-a),var(--photo-b));position:absolute;overflow:hidden}
.photo.warm{background:linear-gradient(135deg,#8a5a3c,#d1a86a)}
.photo.dark{background:linear-gradient(135deg,#3b3a30,#7e7158)}
.play{position:absolute;left:50%;top:50%;width:22px;height:22px;margin:-11px 0 0 -11px;border:1.5px solid #fff;border-radius:50%}
.play::after{content:"";position:absolute;left:8px;top:5px;border-left:7px solid #fff;border-top:5px solid transparent;border-bottom:5px solid transparent}
.btn{display:inline-block;font-size:5px;padding:3px 8px;border-radius:1px;font-weight:500;letter-spacing:.2px}
.btn.dark{background:var(--forest);color:#fff}
.btn.line{border:.8px solid var(--forest);color:var(--forest);background:transparent}
.btn.sage{background:var(--sage);color:var(--forest)}
.abs{position:absolute}
.small{font-size:5.4px;line-height:1.55}
.nav-name{font-family:"Gelasio",serif;font-size:10px;letter-spacing:1px;font-weight:600;color:#fff}
.badge{position:absolute;border-radius:50%;background:var(--coral)}
.step-icon{width:46px;height:46px;border:1.2px solid var(--forest);border-radius:50%;margin:0 auto 10px;display:flex;align-items:center;justify-content:center}
.partner{width:66px;height:34px;background:#fff;display:flex;align-items:center;justify-content:center}
.partner i{display:block;width:34px;height:12px;border-radius:6px;background:#c9cfc4}
.social{width:11px;height:11px;border-radius:50%;background:#fff;display:inline-block}
.icon-line{display:flex;gap:4px;align-items:flex-start}

/* ---------- desktop page ---------- */
.desk{position:absolute;left:158px;top:161px;width:548px;height:2057px;background:var(--blush);overflow:hidden}
.desk .hero{position:absolute;left:0;top:0;width:548px;height:242px;background:var(--forest);color:#fff}
.hero .kicker{font-size:5px;letter-spacing:.5px}
.desk .about-seed{position:absolute;left:0;top:242px;width:548px;height:168px;background:var(--sage);text-align:center}
.desk h2{font-family:"Gelasio",serif;font-weight:400;font-size:15px;color:var(--forest)}
.desk .kit{position:absolute;left:0;top:410px;width:548px;height:280px;background:var(--blush);border-radius:0 0 46px 0;z-index:1}
.desk .manual{position:absolute;left:0;top:679px;width:548px;height:615px;background:var(--sage);border-radius:0 0 0 70px;text-align:center;z-index:0}
.steps{position:absolute;left:48px;top:110px;width:452px;display:flex;justify-content:space-between}
.step{width:100px;text-align:center}
.step h4{font-family:"Gelasio",serif;font-weight:400;font-size:8px;margin-bottom:8px;color:var(--forest)}
.step p{font-size:4.6px;line-height:1.5}
.make-card{position:absolute;left:92px;top:308px;width:364px;height:140px;background:var(--forest);color:#fff;text-align:left}
.make-card h3{font-family:"Gelasio",serif;font-weight:400;font-size:15px;line-height:1.2}
.insta{position:absolute;left:92px;top:1178px;width:364px;text-align:center}
.grid{display:grid;grid-template-columns:repeat(4,86px);gap:6px;margin-top:10px}
.grid div{position:relative;height:86px}
.news{position:absolute;left:0;top:1440px;width:548px;text-align:center}
.collab{position:absolute;left:49px;top:1560px;width:449px;height:104px;background:var(--sage);border-radius:30px 0 30px 0;text-align:center;z-index:2}
.desk .foot{position:absolute;left:0;top:1600px;width:548px;height:457px;background:var(--forest);color:#fff}
.partners{display:flex;gap:10px;justify-content:center}

/* ---------- mobile page ---------- */
.mob{position:absolute;left:874px;top:161px;width:178px;height:3700px;background:var(--blush);overflow:hidden}
.mob > section,.mob > footer{position:relative;width:178px}
.mob h2{font-family:"Gelasio",serif;font-weight:400;font-size:13px;color:var(--forest);line-height:1.2}
.m-hero{height:400px;background:var(--forest);color:#fff;text-align:center}
.m-about{height:225px;background:var(--sage);padding:14px 10px 0}
.m-kit{height:333px;background:var(--blush);border-radius:0 0 0 26px;z-index:1;padding:28px 26px 0}
.m-manual{height:922px;margin-top:-26px;background:var(--sage);padding:62px 10px 0;text-align:center}
.m-step{margin-bottom:16px}
.m-step .step-icon{width:64px;height:64px;margin-bottom:10px}
.m-step h4{font-family:"Gelasio",serif;font-weight:400;font-size:9px;color:var(--forest);margin-bottom:6px}
.m-step p{font-size:5.4px;line-height:1.55;padding:0 8px}
.m-make{height:270px;background:var(--sage)}
.m-make-card{position:absolute;left:6px;top:0;width:166px;height:112px;background:var(--forest);color:#fff;text-align:center;padding:20px 10px 0}
.m-insta{height:380px;text-align:center;padding-top:26px}
.m-insta-grid{display:grid;grid-template-columns:82px 82px;gap:3px;justify-content:center;margin-top:10px}
.m-insta-grid div{position:relative;height:80px}
.m-news{height:170px;text-align:center;padding:0 14px}
.m-collab{height:120px;background:var(--sage);border-radius:22px 0 0 0;text-align:center;padding:0 18px;z-index:2}
.m-foot{height:880px;background:var(--forest);color:#fff}
</style>
</head>
<body>
<div class="backdrop"></div>
<div class="title-mark">TALMATTE</div>

<!-- ================= Desktop ================= -->
<main class="desk">
  <section class="hero">
    <div class="abs nav-name" style="left:48px;top:28px">TALMATTE</div>
    <div class="badge" style="left:456px;top:20px;width:40px;height:40px"></div>
    <div class="abs" style="left:92px;top:86px;width:190px">
      <div class="kicker">WILLKOMMEN IM</div>
      <h1 class="serif" style="font-weight:400;font-size:17px;margin:6px 0 8px">Wohnheim Talmatte</h1>
      <p class="small">einem Ort der Unterstützung und Betreuung für Menschen mit Unterstützungsbedarf. Hier bieten wir differenzierte Tagesbeschäftigungen, individuell angepasste Betreuungsangebote, vielfältige Veranstaltungen und einen Shop mit liebevoll hergestellten Produkten.</p>
      <span class="btn sage" style="margin-top:14px">Erfahre mehr über die Seedbombs →</span>
    </div>
  </section>
  <div class="photo" role="img" aria-label="Video: Bewohnerin formt Seedbombs im Garten" style="left:318px;top:58px;width:230px;height:226px;border-radius:40px 0 40px 0;z-index:3"><span class="play"></span></div>

  <section class="about-seed">
    <h2 style="margin-top:50px">Was sind Seedbombs</h2>
    <p class="small" style="width:360px;margin:10px auto 0">Seedbombs, sind handgefertigte Kugeln aus Ton, Bio-Erde und lokalen, Schweizer Saatgut, die von unseren Bewohner:innen handgefertigt werden. Ursprünglich von nordamerikanischen Umweltschützern genutzt, werden sie heute weltweit im Guerilla Gardening eingesetzt, um brachliegende Flächen im urbanen Raum zu begrünen und Bienen und Insekten Nahrung zu bieten. Für ein gesundes Ökosystem.</p>
  </section>

  <section class="kit">
    <div class="photo" role="img" aria-label="Hand hält eine Seedbomb-Verpackung" style="left:0;top:29px;width:173px;height:153px;border-radius:0 34px 0 0"></div>
    <div class="abs" style="left:207px;top:34px;width:150px">
      <div style="font-size:5.5px">Love ♥ Gardening!</div>
      <h3 class="serif" style="font-size:14px;margin:3px 0 6px">Seedbombs kit</h3>
      <p class="small">A differentiated range of day activities and an individually adapted care setting are aimed at adults …</p>
      <div class="serif" style="font-size:8px;margin:8px 0">$199.00</div>
      <span class="btn dark">Explore seedbombs →</span>
      <span class="btn line" style="margin-left:4px">Add to cart →</span>
    </div>
    <div class="photo dark" role="img" aria-label="Seedbombs trocknen in einem Eierkarton" style="left:372px;top:92px;width:176px;height:141px"></div>
  </section>

  <section class="manual">
    <h2 style="margin-top:38px;line-height:1.3">Anleitung zur Verwendung des<br><b style="font-weight:600">seedbombs</b></h2>
    <div class="steps">
      <div class="step">
        <div class="step-icon"><svg width="22" height="22" viewBox="0 0 24 24" fill="none" stroke="#22392c" stroke-width="1.2"><path d="M4 20c4-1 6-4 8-8"/><circle cx="16" cy="8" r="3"/></svg></div>
        <h4>Pflanzen</h4>
        <p>Wirf die Seedbomb. Du musst sie nicht eingraben. Wirf sie einfach auf die gewählte Fläche. Der Ton schützt das Saatgut vor Vögeln oder anderen Tieren.</p>
      </div>
      <div class="step">
        <div class="step-icon"><svg width="22" height="22" viewBox="0 0 24 24" fill="none" stroke="#22392c" stroke-width="1.2"><circle cx="12" cy="13" r="6"/><path d="M9 4l1 3M13 3v3M16 4l-1 3"/></svg></div>
        <h4>Bewässern</h4>
        <p>Warte auf Regen. Die Seedbomb braucht Wasser, um zu keimen. Wenn es nicht regnet, kannst du die Seedbomb auch manuell giessen.</p>
      </div>
      <div class="step">
        <div class="step-icon"><svg width="22" height="22" viewBox="0 0 24 24" fill="none" stroke="#22392c" stroke-width="1.2"><circle cx="12" cy="12" r="7"/><path d="M12 16V9M12 11c-2 0-3-1-3-3M12 10c2 0 3-1 3-3"/></svg></div>
        <h4>Warten</h4>
        <p>Hab Geduld. Pflanzen brauchen Zeit zum Wachsen. Es kann einige Wochen dauern, bis Du die ersten Triebe siehst.</p>
      </div>
      <div class="step">
        <div class="step-icon"><svg width="22" height="22" viewBox="0 0 24 24" fill="none" stroke="#22392c" stroke-width="1.2"><path d="M12 20V8M12 12l-4-3M12 10l4-3M8 20h8"/></svg></div>
        <h4>Geniessen</h4>
        <p>Beobachte das Wachstum. Über die nächsten Wochen und Monate kannst Du beobachten, wie aus der Seedbomb eine blühende Pflanze wird. Geniesse die Schönheit der Natur.</p>
      </div>
    </div>
    <span class="btn dark abs" style="left:243px;top:260px">Kontaktiere uns →</span>
    <p class="abs" style="left:120px;top:284px;width:308px;font-size:4.6px;line-height:1.5">Bitte beachte, dass Du beim Einsatz von Seedbombs die lokalen Gesetze und Vorschriften beachten solltest, insbesondere wenn Du sie in öffentlichen Bereichen oder auf fremdem Eigentum verwenden möchtest.</p>
    <div class="make-card">
      <div class="abs" style="left:18px;top:24px;width:160px">
        <h3>Wie wir Seedbombs<br>herstellen</h3>
        <p class="small" style="margin-top:8px">Die Seedballs werden in unserer inklusiven Werkstatt im Talmatte hergestellt. Hier kannst du ein Video der Herstellung für unsere Kunden <u>«ERDE &amp; HERZ»</u> sehen.</p>
      </div>
      <div class="photo warm" role="img" aria-label="Video: Hand voller Erde beim Formen einer Seedbomb" style="left:188px;top:0;width:176px;height:140px"><span class="play"></span></div>
    </div>
  </section>

  <section class="insta">
    <div class="serif" style="font-size:12px;color:var(--forest)"><span style="display:inline-block;width:9px;height:9px;border:1px solid var(--forest);border-radius:2px;margin-right:4px"></span>TALMATTE</div>
    <div class="grid">
      <div class="photo warm" role="img" aria-label="Instagram-Bild: Bewohnerin mit Blumen"></div>
      <div class="photo warm" role="img" aria-label="Instagram-Bild: Arbeit in der Werkstatt"></div>
      <div class="photo dark" role="img" aria-label="Instagram-Bild: Keramikgefässe"></div>
      <div class="photo warm" role="img" aria-label="Instagram-Bild: Herbstbaum vor dem Haus"></div>
      <div class="photo" role="img" aria-label="Instagram-Bild: Haus mit Garten"></div>
      <div class="photo warm" role="img" aria-label="Instagram-Bild: Backen am Tisch"></div>
      <div class="photo dark" role="img" aria-label="Instagram-Bild: Gemälde im Rahmen"></div>
      <div class="photo" role="img" aria-label="Instagram-Bild: zwei Personen am Tisch"></div>
    </div>
    <div style="margin-top:20px"><span class="btn line">Folge uns auf Instagram →</span> <span class="btn line" style="margin-left:6px">Folge uns auf Facebook →</span></div>
  </section>

  <section class="news">
    <h2>Abonniere unseren <b style="font-weight:600">Newsletter</b></h2>
    <p class="small" style="width:300px;margin:6px auto 0">Möchtest Du über die aktuellen Geschehnisse im Talmatte auf dem Laufenden bleiben? Dann abonniere Sie unseren Newsletter.</p>
    <div style="width:276px;margin:18px auto 0;display:flex;align-items:flex-end;justify-content:space-between">
      <span style="flex:1;border-bottom:.8px solid var(--forest);font-size:5px;text-align:left;font-style:italic;padding-bottom:2px;margin-right:12px">Geben Deine E-Mail-Adresse ein</span>
      <span class="btn line">Abonnieren →</span>
    </div>
  </section>

  <section class="collab">
    <h2 style="margin-top:-6px;line-height:1.05">Wollen sie mit mit uns<br><b style="font-weight:600">zusammen Arbeiten</b></h2>
    <p style="font-size:6.5px;line-height:1.5;width:270px;margin:6px auto 0">Fragen Sie an mit Ihrer Idee und wir helfen Ihnen bei der inklusiven Umsetzung Ihres Projekts</p>
    <span class="btn line" style="margin-top:8px">Jetzt anfragen →</span>
  </section>

  <footer class="foot">
    <div class="serif" style="position:absolute;left:0;top:70px;width:548px;text-align:center;font-size:10px">Partner:</div>
    <div class="partners" style="position:absolute;left:0;width:548px;top:92px">
      <div class="partner"><i></i></div><div class="partner"><i></i></div><div class="partner"><i></i></div><div class="partner"><i></i></div><div class="partner"><i></i></div>
    </div>
    <div class="photo" role="img" aria-label="Bewohnende und Betreuer bei der Gartenarbeit" style="left:92px;top:163px;width:146px;height:146px;border-radius:22px 0 22px 0;border:1px solid #fff"></div>
    <div class="abs" style="left:279px;top:178px;width:170px">
      <h3 class="serif" style="font-weight:400;font-size:14px">Über <b style="font-weight:600">uns</b></h3>
      <p class="small" style="margin-top:8px">Das Talmatte ist ein Wohnheim, eine Arbeitsstelle und eine Werkstatt für Menschen mit einer Behinderung in Liestal und bietet aktuell Wohnplätze für 17 Menschen. Das Beschäftigungsangebot steht auch Menschen zur Verfügung, die ausserhalb des Talmatte wohnen. Die Bewohner:innen betätigen sich in der Hauswirtschaft, der Werkstatt und dem Garten mit den Tieren …</p>
      <span class="btn sage" style="margin-top:8px">Entdecken Sie Über uns →</span>
    </div>
    <div class="abs" style="left:92px;top:354px">
      <div class="nav-name" style="font-size:15px">TALMATTE</div>
      <div style="font-size:4.5px;margin-top:10px">© 2023 Talmatte. All Rights Reserved.</div>
    </div>
    <div class="abs" style="left:226px;top:356px;width:100px;font-size:4.8px;line-height:1.7">
      <div class="serif" style="font-size:8px;margin-bottom:6px">Kontakt</div>
      <div>☏ 0041 61 555 01 20</div>
      <div>✉ info@talmatte-kollektiv.ch</div>
      <div class="icon-line"><svg width="5" height="6" viewBox="0 0 10 12"><path d="M5 0a4 4 0 0 1 4 4c0 3-4 8-4 8S1 7 1 4a4 4 0 0 1 4-4z" fill="#fff"/></svg><span>Talmatte<br>Lindenweg 14<br>4410 Liestal</span></div>
    </div>
    <div class="abs" style="left:323px;top:356px;width:110px;font-size:4.8px;line-height:1.7">
      <div class="serif" style="font-size:8px;margin-bottom:6px">Bürozeiten</div>
      <div>Montag - Freitag<br>09:00 bis 12:00 Uhr &amp; 13:00 bis 17:00 Uhr</div>
      <span class="btn sage" style="margin-top:6px">Jetzt Spenden →</span>
    </div>
    <div class="abs" style="left:441px;top:354px"><span class="social"></span><br><span class="social" style="margin-top:3px"></span></div>
  </footer>
</main>

<!-- ================= Mobile ================= -->
<main class="mob">
  <section class="m-hero">
    <div class="abs nav-name" style="left:10px;top:22px">TALMATTE</div>
    <div class="badge" style="left:138px;top:14px;width:32px;height:32px"></div>
    <div style="padding:78px 14px 0">
      <div style="font-size:5px;letter-spacing:.5px">WILLKOMMEN IM</div>
      <h1 class="serif" style="font-weight:400;font-size:15px;margin:4px 0 8px">Wohnheim Talmatte</h1>
      <p class="small">einem Ort der Unterstützung und Betreuung für Menschen mit Unterstützungsbedarf. Hier bieten wir differenzierte Tagesbeschäftigungen, individuell angepasste Betreuungsangebote, vielfältige Veranstaltungen und einen Shop mit liebevoll hergestellten Produkten.</p>
      <span class="btn sage" style="margin-top:12px">Erfahre mehr über die Seedbombs ↓</span>
    </div>
    <div class="photo" role="img" aria-label="Video: Bewohnerin formt Seedbombs im Garten" style="left:10px;top:238px;width:158px;height:155px;border-radius:24px 0 24px 0"><span class="play"></span></div>
  </section>

  <section class="m-about">
    <h2>Was sind Seedbombs</h2>
    <p class="small" style="margin-top:8px;font-size:5.6px;line-height:1.75">Seedbombs, sind handgefertigte Kugeln aus Ton, Bio-Erde und lokalen, Schweizer Saatgut, die von unseren Bewohner:innen handgefertigt werden. Ursprünglich von nordamerikanischen Umweltschützern genutzt, werden sie heute weltweit im Guerilla Gardening eingesetzt, um brachliegende Flächen im urbanen Raum zu begrünen und Bienen und Insekten Nahrung zu bieten. Für ein gesundes Ökosystem.</p>
  </section>

  <section class="m-kit">
    <div style="font-size:5.5px">Love ♥ Gardening!</div>
    <h3 class="serif" style="font-size:12px;margin:2px 0 4px">Seedbombs kit</h3>
    <p class="small">A differentiated range of day activities and an individually adapted care setting are aimed at adults …</p>
    <div class="serif" style="font-size:7px;margin:8px 0 5px">$199.00</div>
    <span class="btn dark">Explore seedbombs →</span><br>
    <span class="btn line" style="margin-top:5px">Add to cart →</span>
    <div class="photo" role="img" aria-label="Hand hält eine Seedbomb-Verpackung" style="left:0;top:180px;width:90px;height:92px;border-radius:0 18px 0 0"></div>
    <div class="photo dark" role="img" aria-label="Seedbombs trocknen in einem Eierkarton" style="left:94px;top:198px;width:84px;height:90px"></div>
  </section>

  <section class="m-manual">
    <h2>Anleitung zur<br>Verwendung des<br><b style="font-weight:600">seedbombs</b></h2>
    <div style="margin-top:18px">
      <div class="m-step"><div class="step-icon"><svg width="28" height="28" viewBox="0 0 24 24" fill="none" stroke="#22392c" stroke-width="1"><path d="M4 20c4-1 6-4 8-8"/><circle cx="16" cy="8" r="3"/></svg></div><h4>Pflanzen</h4><p>Wirf die Seedbomb. Du musst sie nicht eingraben. Wirf sie einfach auf die gewählte Fläche. Der Ton schützt das Saatgut vor Vögeln oder anderen Tieren.</p></div>
      <div class="m-step"><div class="step-icon"><svg width="28" height="28" viewBox="0 0 24 24" fill="none" stroke="#22392c" stroke-width="1"><circle cx="12" cy="13" r="6"/><path d="M9 4l1 3M13 3v3M16 4l-1 3"/></svg></div><h4>Bewässern</h4><p>Warte auf Regen. Die Seedbomb braucht Wasser, um zu keimen. Wenn es nicht regnet, kannst Du die Seedbomb auch manuell giessen.</p></div>
      <div class="m-step"><div class="step-icon"><svg width="28" height="28" viewBox="0 0 24 24" fill="none" stroke="#22392c" stroke-width="1"><circle cx="12" cy="12" r="7"/><path d="M12 16V9M12 11c-2 0-3-1-3-3M12 10c2 0 3-1 3-3"/></svg></div><h4>Warten</h4><p>Hab Geduld. Pflanzen brauchen Zeit zum Wachsen. Es kann einige Wochen dauern, bis Du die ersten Triebe siehst.</p></div>
      <div class="m-step"><div class="step-icon"><svg width="28" height="28" viewBox="0 0 24 24" fill="none" stroke="#22392c" stroke-width="1"><path d="M12 20V8M12 12l-4-3M12 10l4-3M8 20h8"/></svg></div><h4>Geniessen</h4><p>Beobachte das Wachstum. Über die nächsten Wochen und Monate kannst Du beobachten, wie aus der Seedbomb eine blühende Pflanze wird. Geniesse die Schönheit der Natur und die Freude, die Du den Bienen und Insekten bereitet hast.</p></div>
    </div>
    <span class="btn dark" style="margin-top:6px">Kontaktiere uns →</span>
    <p style="font-size:5px;line-height:1.6;margin-top:18px;padding:0 6px">Bitte beachte, dass Du beim Einsatz von Seedbombs die lokalen Gesetze und Vorschriften beachten solltest, insbesondere wenn Du sie in öffentlichen Bereichen oder auf fremdem Eigentum verwenden möchtest.</p>
  </section>

  <section class="m-make">
    <div class="m-make-card">
      <h3 class="serif" style="font-weight:400;font-size:13px;line-height:1.2">Wie wir Seedbombs<br><b style="font-weight:600">herstellen</b></h3>
      <p class="small" style="margin-top:6px">Die Seedballs werden in unserer inklusiven Werkstatt im Talmatte hergestellt. Hier kannst du ein Video der Herstellung für unsere Kunden «ERDE &amp; HERZ» sehen.</p>
    </div>
    <div class="photo warm" role="img" aria-label="Video: Hand voller Erde beim Formen einer Seedbomb" style="left:10px;top:112px;width:158px;height:128px;border-radius:0 0 0 22px"><span class="play"></span></div>
  </section>

  <section class="m-insta">
    <div class="serif" style="font-size:12px;color:var(--forest)"><span style="display:inline-block;width:9px;height:9px;border:1px solid var(--forest);border-radius:2px;margin-right:3px"></span>TALMATTE</div>
    <div class="m-insta-grid">
      <div class="photo warm" role="img" aria-label="Instagram-Bild: Bewohnerin mit Blumen"></div>
      <div class="photo warm" role="img" aria-label="Instagram-Bild: Arbeit in der Werkstatt"></div>
      <div class="photo dark" role="img" aria-label="Instagram-Bild: Keramikgefässe"></div>
      <div class="photo warm" role="img" aria-label="Instagram-Bild: Herbstbaum vor dem Haus"></div>
      <div class="photo" role="img" aria-label="Instagram-Bild: Haus mit Garten"></div>
      <div class="photo warm" role="img" aria-label="Instagram-Bild: Backen am Tisch"></div>
    </div>
    <span class="btn line" style="margin-top:20px;padding:4px 16px">Folge uns auf Instagram →</span><br>
    <span class="btn line" style="margin-top:10px;padding:4px 16px">Folge uns auf Facebook →</span>
  </section>

  <section class="m-news">
    <h2>Abonniere unseren<br><b style="font-weight:600">Newsletter</b></h2>
    <p class="small" style="margin-top:6px">Möchten Sie über die aktuellen Geschehnisse im Talmatte auf dem Laufenden bleiben? Dann abonnieren Sie unseren Newsletter.</p>
    <div style="border-bottom:.8px solid var(--forest);font-size:5px;font-style:italic;margin-top:18px;padding-bottom:2px">Geben Sie Ihre E-Mail-Adresse ein</div>
    <span class="btn line" style="margin-top:12px;padding:4px 14px">Abonnieren →</span>
  </section>

  <section class="m-collab">
    <h2 style="margin-top:-4px;font-size:11px;line-height:1.1;position:relative;top:-8px">Wollen sie mit mit uns<br><b style="font-weight:600">zusammen Arbeiten</b></h2>
    <p style="font-size:6.2px;line-height:1.55;margin-top:4px">Fragen Sie an mit Ihrer Idee und wir helfen Ihnen bei der inklusiven Umsetzung Ihres Projekts</p>
    <span class="btn line" style="margin-top:10px;padding:4px 14px">Jetzt anfragen →</span>
  </section>

  <footer class="m-foot">
    <div class="serif" style="text-align:center;font-size:11px;padding-top:40px">Partner:</div>
    <div style="display:flex;gap:10px;justify-content:center;margin-top:10px">
      <div class="partner" style="width:74px;height:40px"><i></i></div><div class="partner" style="width:74px;height:40px"><i></i></div>
    </div>
    <div class="photo" role="img" aria-label="Bewohnende und Betreuer bei der Gartenarbeit" style="left:10px;top:140px;width:158px;height:172px;border-radius:24px 0 24px 0;border:1px solid #fff"></div>
    <div class="abs" style="left:18px;top:334px;width:145px">
      <h3 class="serif" style="font-weight:400;font-size:14px">Über <b style="font-weight:600">uns</b></h3>
      <p class="small" style="margin-top:8px">Das Talmatte ist ein Wohnheim, eine Arbeitsstelle und eine Werkstatt für Menschen mit einer Behinderung in Liestal und bietet aktuell Wohnplätze für 17 Menschen. Das Beschäftigungsangebot steht auch Menschen zur Verfügung, die ausserhalb wohnen …</p>
      <span class="btn sage" style="margin-top:10px;padding:4px 10px">Entdecken Sie Über uns →</span>
    </div>
    <div class="abs" style="left:10px;top:470px;width:158px;font-size:5.4px;line-height:1.7">
      <div class="nav-name" style="font-size:17px">TALMATTE</div>
      <div class="serif" style="font-size:10px;margin:18px 0 10px">Kontakt</div>
      <div>☏ &nbsp;0041 61 555 01 20</div>
      <div style="margin-top:10px">✉ &nbsp;info@talmatte-kollektiv.ch</div>
      <div class="icon-line" style="margin-top:10px"><svg width="6" height="7" viewBox="0 0 10 12"><path d="M5 0a4 4 0 0 1 4 4c0 3-4 8-4 8S1 7 1 4a4 4 0 0 1 4-4z" fill="#fff"/></svg><span>Talmatte<br>Lindenweg 14<br>4410 Liestal</span></div>
      <div class="serif" style="font-size:10px;margin:20px 0 6px">Bürozeiten</div>
      <div>Montag - Freitag<br>09:00 bis 12:00 Uhr &amp; 13:00 bis 17:00 Uhr</div>
      <span class="btn sage" style="margin-top:10px;padding:4px 10px">Jetzt Spenden →</span>
      <div style="text-align:center;margin-top:22px"><span class="social" style="width:13px;height:13px"></span> <span class="social" style="width:13px;height:13px;margin-left:4px"></span></div>
      <div style="text-align:center;font-size:4.8px;margin-top:22px">© 2023 Talmatte. All Rights Reserved.</div>
    </div>
  </footer>
</main>
</body>
</html>
```